Corvellan Solutions needs an IT Managed Services Website and the logo needs to be updated

We need a new website for our 25 year old IT Managed Services Company. Our company specializes in listening to and understanding our customer needs and goals. Our customers include SME's and Corporates in industries ranging from Medical, Legal, Industrial & Manufacturing and Financial. The services that we offer include: Managed IT Services, Remote Monitoring and Management and Virtualisation. Corvellan Solutions takes technology and makes the lives of our customers easier by applying it appropriately. In the same way, we want a website that is as pleasing to the eye, as it is simple to find information and call to action. The website should say as much in design as it does in content and it should be saying that Corvellan Solutions is your technology partner that listens to you, understands you, delivers solutions and is loyal in our relationship with you. Aesthetically, we want to go for something a little warmer than blue and white, but want to err on the side of professional.
The Logo: We need the "computer" and "ltd" to be removed from the logo. We want to keep the @ on the "u". We would like to freshen up the logo inline with the website design in terms of look and feel and colour.

Target Market(s)

Businesses that require IT Managed Services

Logo Text

Corvellan Solutions

Coding

Coded - Design and coding required

Number of Pages Required

5+ page

Font styles to use
Sans Serif

Colors

Designer to choose colors to be used in the design.

Requirements
Must have
• Each page must have a call to action.

```html
<!DOCTYPE html>
<html lang="en">
<head>
<meta charset="utf-8">
<title>Corvellan Solutions – IT Managed Services</title>
<link href="https://fonts.googleapis.com/css2?family=Montserrat:wght@400;500;600;700&family=Open+Sans:wght@400;600;700;800&display=swap" rel="stylesheet">
<style>
:root{
  --orange:#f9a51a;
  --orange-light:#fdb933;
  --ink:#222222;
  --text:#3d3d3d;
  --panel:#f3f2f2;
  --white:#ffffff;
  --footer:#141414;
  --hero-a:#0b1f45;
  --hero-b:#1f4e8f;
}
*{box-sizing:border-box;margin:0;padding:0}
html,body{width:1200px;height:3896px;overflow:hidden;background:var(--white)}
body{position:relative;font-family:"Open Sans",Arial,sans-serif;color:var(--text)}
.abs{position:absolute}

/* header */
.site-header{position:absolute;left:0;top:0;width:1200px;height:99px;background:var(--white)}
.brand{position:absolute;display:flex;align-items:center;gap:10px;font-family:"Montserrat",Arial,sans-serif;font-weight:600;color:var(--orange);white-space:nowrap}
.brand .dot{width:34px;height:34px;border-radius:50%;background:var(--orange);flex:none}
.site-header .brand{left:130px;top:29px;font-size:24px}
.main-nav{position:absolute;left:493px;top:31px;display:flex;gap:26px;align-items:center}
.main-nav a{font-size:13px;font-weight:700;color:var(--ink);text-decoration:none;text-transform:uppercase;padding:8px 0}
.main-nav a.active{background:var(--orange);color:var(--white);padding:8px 16px}
.call-us{position:absolute;left:893px;top:28px;display:flex;align-items:center;gap:12px}
.call-us .ring{width:36px;height:36px;border:2px solid var(--orange);border-radius:50%;display:flex;align-items:center;justify-content:center}
.call-us small{display:block;font-size:11px;font-weight:700;color:var(--ink)}
.call-us strong{display:block;font-size:22px;font-weight:700;color:var(--orange);line-height:1}

/* hero */
.hero{position:absolute;left:0;top:99px;width:1200px;height:550px;background:linear-gradient(180deg,#1a2d55 0%,var(--hero-b) 45%,var(--hero-a) 100%)}
.hero h1{position:absolute;left:0;top:180px;width:1200px;text-align:center;color:var(--white);font-weight:800;font-size:40px;line-height:52px;text-transform:uppercase;text-shadow:0 2px 6px rgba(0,0,0,.5)}
.hero-arrow{position:absolute;top:235px;width:40px;height:44px;background:rgba(60,60,60,.8);display:flex;align-items:center;justify-content:center}
.btn{position:absolute;display:flex;align-items:center;justify-content:center;background:var(--orange);color:var(--white);font-weight:700;font-size:14px;text-transform:uppercase;letter-spacing:.3px}

/* illustration areas */
.art{position:absolute;border-radius:14px;box-shadow:0 10px 24px rgba(0,0,0,.12)}
.art-welcome{left:166px;top:724px;width:304px;height:227px;background:linear-gradient(160deg,#fff4de 0%,#ffe3b0 55%,#e9e2f3 100%)}
.art-managed{left:130px;top:270px;width:420px;height:380px;background:linear-gradient(160deg,#ffffff 0%,#e4e9f1 60%,#c9d3e2 100%)}
.art-rmm{left:640px;top:770px;width:460px;height:350px;background:linear-gradient(150deg,#8a5ad6 0%,#5b6fe0 55%,#e9ecf7 100%)}
.art-virtual{left:60px;top:1410px;width:500px;height:370px;background:linear-gradient(150deg,#e9f1f6 0%,#6b7f96 55%,#2e3440 100%)}

/* welcome */
.welcome-rule{position:absolute;left:540px;top:714px;width:4px;height:247px;background:#dcdcdc}
.eyebrow{position:absolute;left:607px;top:726px;font-family:"Montserrat",Arial,sans-serif;font-size:18px;font-weight:500;color:var(--ink)}
.welcome-title{position:absolute;left:605px;top:752px;font-family:"Montserrat",Arial,sans-serif;font-size:36px;font-weight:700;color:var(--ink);letter-spacing:1px}
.copy{font-size:12.5px;line-height:21px;color:var(--text)}
.welcome-copy{position:absolute;left:607px;top:826px;width:445px}

/* services */
.services{position:absolute;left:0;top:1044px;width:1200px;height:1976px;background:var(--panel);overflow:hidden}
.section-title{position:absolute;left:0;width:1200px;text-align:center;font-family:"Montserrat",Arial,sans-serif;font-weight:700;font-size:23px;color:var(--ink)}
.title-rule{position:absolute;left:578px;width:44px;height:3px;background:#c8c8c8}
.service-title{position:absolute;font-family:"Montserrat",Arial,sans-serif;font-size:27px;font-weight:500;color:var(--ink);line-height:34px}
.service-copy{position:absolute;width:405px}

/* why us */
.why-mark{position:absolute;left:215px;top:3110px;width:230px;display:flex;flex-direction:column;align-items:center;gap:18px;font-family:"Montserrat",Arial,sans-serif;font-weight:700;font-size:34px;color:var(--orange)}
.why-mark .dot{width:130px;height:130px;border-radius:50%;background:var(--orange)}
.why-title{position:absolute;left:541px;top:3093px;font-family:"Montserrat",Arial,sans-serif;font-size:27px;font-weight:500;color:var(--ink)}
.why-copy{position:absolute;left:543px;top:3156px;width:465px}
.why-copy p{margin-bottom:21px}

/* footer */
.site-footer{position:absolute;left:0;top:3519px;width:1200px;height:377px;background:linear-gradient(180deg,#1c1c1c,var(--footer));color:#d6d6d6}
.site-footer .brand{left:130px;top:112px;font-size:20px}
.site-footer .brand .dot{width:28px;height:28px}
.foot-col{position:absolute;top:72px;font-size:12px;line-height:18px}
.foot-col h4{font-size:12px;font-weight:700;color:var(--white);text-transform:uppercase;margin-bottom:16px}
.foot-line{display:flex;align-items:flex-start;gap:12px;margin-bottom:18px}
.menu-list{list-style:none}
.social{display:flex;align-items:center;gap:12px;margin-bottom:14px}
.social .dot{width:24px;height:24px;border-radius:50%;background:#2f6fc2}
.foot-rule{position:absolute;left:130px;top:272px;width:940px;height:1px;background:#333}
.copyright{position:absolute;left:0;top:311px;width:1200px;text-align:center;font-size:12px;color:#cfcfcf}
</style>
</head>
<body>

<header class="site-header">
  <div class="brand"><span class="dot"></span>Corvellan Solutions</div>
  <nav class="main-nav">
    <a class="active">Home</a>
    <a>Why Us</a>
    <a>Services</a>
    <a>Contact Us</a>
  </nav>
  <div class="call-us">
    <span class="ring">
      <svg width="18" height="18" viewBox="0 0 24 24"><path fill="#f9a51a" d="M6.6 10.8a15.1 15.1 0 0 0 6.6 6.6l2.2-2.2a1 1 0 0 1 1-.25 11.4 11.4 0 0 0 3.6.57 1 1 0 0 1 1 1V20a1 1 0 0 1-1 1A17 17 0 0 1 3 4a1 1 0 0 1 1-1h3.5a1 1 0 0 1 1 1c0 1.25.2 2.45.57 3.57a1 1 0 0 1-.25 1z"/></svg>
    </span>
    <div><small>CALL US</small><strong>555.014.2260</strong></div>
  </div>
</header>

<section class="hero" role="img" aria-label="Photograph of a brightly lit server room corridor">
  <h1>Free choices become<br>the matrix of human life</h1>
  <a class="btn" style="left:504px;top:306px;width:153px;height:44px">Read More</a>
  <span class="hero-arrow" style="left:0"><svg width="12" height="16" viewBox="0 0 12 16"><path d="M10 1 3 8l7 7" fill="none" stroke="#fff" stroke-width="2.5"/></svg></span>
  <span class="hero-arrow" style="left:1160px"><svg width="12" height="16" viewBox="0 0 12 16"><path d="m2 1 7 7-7 7" fill="none" stroke="#fff" stroke-width="2.5"/></svg></span>
</section>

<section class="welcome">
  <div class="art art-welcome" role="img" aria-label="Illustration of a consultant working at a laptop beside a wall clock"></div>
  <div class="welcome-rule"></div>
  <div class="eyebrow">WELCOME TO</div>
  <div class="welcome-title">CORVELLAN</div>
  <p class="copy welcome-copy">Corvellan Solutions is an IT Managed Services Provider (MSP) that has more than 25 years experience growing and collaborating in the IT Industry. Our expertise lies in listening to and understanding our more than 1000 customers' needs and delivering the best value for money IT Infrastructure and Technology solutions. We believe in loyal and lasting relationships creating a matrix within which your company can grow and outperform it's own expectations.</p>
</section>

<section class="services">
  <svg class="abs" style="left:0;top:0" width="1200" height="1976" viewBox="0 1044 1200 1976">
    <defs>
      <linearGradient id="band" x1="0" y1="0" x2="1" y2="1">
        <stop offset="0" stop-color="#fdbb36"/><stop offset="1" stop-color="#f7a01a"/>
      </linearGradient>
    </defs>
    <polygon points="0,1143 571,1467 0,1870" fill="url(#band)"/>
    <polygon points="1200,1701 623,2052 1200,2428" fill="url(#band)"/>
    <polygon points="0,2272 571,2623 0,2987" fill="url(#band)"/>
  </svg>

  <div class="section-title" style="top:73px">OUR SERVICES</div>
  <div class="title-rule" style="top:124px"></div>

  <div class="art art-managed" role="img" aria-label="Illustration of a business consultant surrounded by reports, charts and screens"></div>
  <div class="service-title" style="left:662px;top:284px">Managed IT Services</div>
  <p class="copy service-copy" style="left:664px;top:343px">Corvellan brings a personal touch to you through our IT consulting services. We collaborate with partners across the globe to bring the best technology to you. You can rely on our expertise to design and maintain the most effective infrastructure for your business.Our quick and efficient Support team will troubleshoot your IT problems and ensure your business continues to operate with minimum disruption.</p>
  <a class="btn" style="left:670px;top:501px;width:197px;height:45px">Contact Us Now</a>

  <div class="art art-rmm" role="img" aria-label="Illustration of a person monitoring dashboards on a large isometric screen"></div>
  <div class="service-title" style="left:174px;top:852px">Remote Monitoring &amp;<br>Management</div>
  <p class="copy service-copy" style="left:176px;top:942px">Corvellan brings you an all-encompassing service that includes managed antivirus, web protection, backup &amp; recovery and email security. You will be able to manage all devices including mobile and you will have active discovery on the network – identifying and managing all new devices that come onto the network.</p>
  <a class="btn" style="left:177px;top:1073px;width:200px;height:44px">Contact Us Now</a>

  <div class="art art-virtual" role="img" aria-label="Illustration of laptops and devices connected to a central server stack"></div>
  <div class="service-title" style="left:670px;top:1432px">Virtualisation</div>
  <p class="copy service-copy" style="left:672px;top:1491px">Corvellan brings you the high performance Hyper Cloud, which reduces your total IT spend in comparison to competitors like Nimbara, Stratocloud and Vaultline. You will find that these Virtual Machines are easy to configure and migration is simple. With Enterprise Grade security and compliance you will have peace of mind about your data.</p>
  <a class="btn" style="left:673px;top:1657px;width:199px;height:44px">Contact Us Now</a>
</section>

<section class="why-us">
  <div class="why-mark"><span class="dot"></span>Corvellan</div>
  <div class="why-title">Why Us</div>
  <div class="copy why-copy">
    <p>Corvellan Solutions was founded in 2000 and is in the business of collaborating with partners to bring the best technologies to you.</p>
    <p>We have more than 25 years experience in the IT industry, servicing customers across the GTA and Ontario. Our customers come from different industry sectors including Medical, Financial, Real Estate, Legal and more. We work together with our customers as members of their teams to realize their IT visions and goals.</p>
    <p>We have collaborated with partners across the globe to ensure that we bring the most innovate and functional technology to our customers. We can proudly say that we offer the best Value for Money solutions.</p>
  </div>
  <a class="btn" style="left:545px;top:3428px;width:141px;height:43px">Read More</a>
</section>

<footer class="site-footer">
  <div class="brand"><span class="dot"></span>Corvellan Solutions</div>
  <div class="foot-col" style="left:455px">
    <h4>Contact Us</h4>
    <div class="foot-line"><svg width="10" height="14" viewBox="0 0 10 14"><path fill="#fff" d="M5 0a5 5 0 0 0-5 5c0 3.6 5 9 5 9s5-5.4 5-9a5 5 0 0 0-5-5zm0 7a2 2 0 1 1 0-4 2 2 0 0 1 0 4z"/></svg><span>17 Harbor Lane<br>Brookfield, IL 60999</span></div>
    <div class="foot-line"><svg width="12" height="12" viewBox="0 0 24 24"><path fill="#fff" d="M6.6 10.8a15.1 15.1 0 0 0 6.6 6.6l2.2-2.2a1 1 0 0 1 1-.25 11.4 11.4 0 0 0 3.6.57 1 1 0 0 1 1 1V20a1 1 0 0 1-1 1A17 17 0 0 1 3 4a1 1 0 0 1 1-1h3.5a1 1 0 0 1 1 1c0 1.25.2 2.45.57 3.57a1 1 0 0 1-.25 1z"/></svg><span>555.014.2260</span></div>
    <div class="foot-line"><svg width="13" height="10" viewBox="0 0 13 10"><rect x=".5" y=".5" width="12" height="9" fill="#fff"/><path d="M.5.5 6.5 5l6-4.5" fill="none" stroke="#141414"/></svg><span>info@corvellan.example</span></div>
  </div>
  <div class="foot-col" style="left:722px">
    <h4>Menu</h4>
    <ul class="menu-list"><li>Home</li><li>About Us</li><li>Services</li><li>Contact us</li></ul>
  </div>
  <div class="foot-col" style="left:953px">
    <h4>Connect With Us</h4>
    <div class="social"><span class="dot"></span>Chatterly</div>
    <div class="social"><span class="dot" style="background:#3aa3e3"></span>Pingbird</div>
    <div class="social"><span class="dot" style="background:#2a5e9c"></span>Workfolio</div>
  </div>
  <div class="foot-rule"></div>
  <div class="copyright">Copyrights @ 2018 All Rights Reserved</div>
</footer>

</body>
</html>
```